Plakat für Hersteller von Maultaschen und Knödeln
Zielgruppe
Mit meiner Manufaktur Kornbeutel & Co stelle ich Maultaschen und Knödel her. Produziert wird mit hochwertigen, möglichst regionalen Zutaten und mit dem Anspruch, traditionelle Klassiker in zeitgemäßer Qualität anzubieten.
Im Mittelpunkt stehen Frische, Transparenz und ehrliches Handwerk. Die Produkte werden mit Sorgfalt hergestellt und sind für den direkten Verkauf auf dem Lindauer Grünmarkt bestimmt. Kornbeutel & Co verbindet bodenständige Küche mit regionaler Identität – unkompliziert, authentisch und genussorientiert.
Zielgruppe rund um den Lindauer Grünmarkt:
- Marktbesucher mit Qualitätsbewusstsein, die gezielt regionale und handwerklich hergestellte Lebensmittel kaufen
- Berufstätige und Familien, die hochwertige, frisch produzierte Gerichte für zu Hause suchen
- Genussorientierte Kundinnen und Kunden, die traditionelle Küche schätzen
- Seniorinnen und Senioren, die klassische Hausmannskost bevorzugen
- Regionalverbundenen Verbraucherinnen und Verbrauchern, die lokale Anbieter unterstützen möchten
Der Lindauer Grünmarkt zieht ein vielfältiges Publikum an, das Wert auf persönliche Beratung, Frische und nachvollziehbare Herkunft legt. Kornbeutel positioniert sich hier als authentischer, spezialisierter Anbieter für handgemachte Teigklassiker mit klarem kulinarischem Profil.
Aufgabenstellung
Das Plakat soll in A5, A4, A3 und A2 nutzbar sein und der Text soll austauschbar sein.
Das Plakat soll gut zum Wochenmarkt passen und ehrliches, qualitativ hochwertiges Handwerk ausdrücken und vor allem Lust auf Maultaschen und Knödel machen. Es soll zu meinen Marktstand (Monza Rot) und dem Logo passen. Das Logo soll sehr präsent sein.

```html
<!DOCTYPE html>
<html lang="de">
<head>
<meta charset="utf-8">
<title>Kornbeutel &amp; Co – Maultaschen &amp; Knödel</title>
<link rel="stylesheet" href="https://fonts.googleapis.com/css2?family=Anton&family=Open+Sans:wght@400;500;600;700&display=swap">
<style>
  :root {
    --monza-red: #b01722;
    --fresh-green: #8dbb24;
    --badge-orange: #f7ab0a;
    --cream: #fff;
    --dough-light: #e9d9b8;
    --dough-dark: #b98a55;
  }
  * { margin: 0; padding: 0; box-sizing: border-box; }
  html, body { width: 848px; height: 1200px; overflow: hidden; }
  body { background: var(--monza-red); }
  .poster {
    position: relative;
    width: 848px;
    height: 1200px;
    background: var(--monza-red);
    font-family: "Open Sans", sans-serif;
    color: var(--cream);
  }
  .headline {
    position: absolute;
    top: 50px;
    left: 0;
    width: 100%;
    text-align: center;
    font-family: "Anton", sans-serif;
    font-weight: 400;
    color: var(--fresh-green);
    text-transform: uppercase;
    font-size: 130px;
    line-height: 158px;
    letter-spacing: 3px;
    white-space: nowrap;
  }
  .headline span { display: block; }
  .subline {
    position: absolute;
    top: 366px;
    left: 0;
    width: 100%;
    text-align: center;
    font-weight: 500;
    font-size: 30px;
    line-height: 42px;
    letter-spacing: 0.5px;
  }
  .product-visual {
    position: absolute;
    left: 157px;
    top: 537px;
    width: 490px;
    height: 362px;
    background: radial-gradient(ellipse 60% 55% at 52% 50%, var(--dough-light) 0%, #d8bf92 45%, var(--dough-dark) 70%, rgba(176,23,34,0) 100%);
  }
  .badge {
    position: absolute;
    left: 569px;
    top: 494px;
    width: 196px;
    height: 196px;
  }
  .badge-text {
    position: absolute;
    inset: 0;
    display: flex;
    flex-direction: column;
    align-items: center;
    justify-content: center;
    font-weight: 700;
    font-size: 29px;
    line-height: 33px;
    color: var(--cream);
    transform: rotate(-8deg);
  }
  .brand {
    position: absolute;
    top: 1000px;
    left: 0;
    width: 100%;
    display: flex;
    align-items: center;
    justify-content: center;
    gap: 24px;
  }
  .brand-dot {
    width: 60px;
    height: 60px;
    border-radius: 50%;
    background: var(--fresh-green);
  }
  .brand-name {
    font-weight: 400;
    font-size: 64px;
    line-height: 1;
    color: var(--cream);
    letter-spacing: -0.5px;
  }
</style>
</head>
<body>
  <main class="poster">
    <h1 class="headline">
      <span>Maultaschen</span>
      <span>&amp; Knödel</span>
    </h1>

    <p class="subline">Handgemachte Klassiker –<br>zum Mitnehmen oder heiß genießen</p>

    <div class="product-visual" role="img" aria-label="Foto: drei Semmelknödel mit Kräutern, Walnusskrumen und Petersilie auf rotem Grund"></div>

    <div class="badge">
      <svg width="196" height="196" viewBox="-100 -100 200 200" aria-hidden="true">
        <polygon fill="var(--badge-orange)" stroke="#fff" stroke-width="2"
          points="0,-96 16,-83 36,-89 44,-70 65,-66 64,-45 82,-33 74,-14 88,3 73,17 78,38 58,45 55,66 34,67 23,85 4,76 -15,89 -29,73 -50,77 -56,57 -76,50 -71,29 -87,15 -72,-1 -82,-20 -64,-31 -66,-52 -45,-57 -38,-77 -18,-73"/>
      </svg>
      <div class="badge-text"><span>Jetzt</span><span>probieren</span></div>
    </div>

    <div class="brand">
      <span class="brand-dot" aria-hidden="true"></span>
      <span class="brand-name">Kornbeutel &amp; Co</span>
    </div>
  </main>
</body>
</html>
```